Perfect — here’s the updated version of your description with **title #1** and the integration/booking functionality references removed, while still keeping the “motivation to book” idea in the design style:
---
**Luxury Property Website Design – Dominican Republic**
We are looking to create a professional and visually appealing **website design** for a premium property that we will be promoting as a short-term rental.
The property is located in an **exclusive area of the Dominican Republic** and offers a high-end experience for guests. Our goal is to create a website that highlights the **luxury, comfort, and exclusivity** of the property, while motivating visitors to **make a reservation inquiry**.
**Key Requirements:**
* A clean, modern, and elegant design that reflects the **premium nature** of the property.
* High-quality visual presentation of the **property’s best features** (rooms, amenities, location, views, nearby attractions).
* Easy-to-navigate structure
* Mobile-friendly and optimized for all screen sizes.
* Space for testimonials or guest reviews to build trust.
**Design Style We Like:**
* Elegant and sophisticated, with a touch of tropical luxury.
* Use of high-quality photography, subtle animations, and a warm color palette that reflects the Caribbean atmosphere.
* A premium feel, similar to boutique hotel or luxury villa rental websites.
**Deliverables:**
* Homepage design.
* Property detail page design (with gallery, amenities, and booking inquiry section).
Contact page or About Us page
* Photo Gallery
The final design should capture the essence of a **luxury getaway** and make visitors feel compelled to reserve their night.

```html
<!DOCTYPE html>
<html lang="en">
<head>
<meta charset="utf-8">
<title>Casa Brisa – Luxury Villa, Dominican Republic</title>
<link href="https://fonts.googleapis.com/css2?family=Exo+2:wght@600;700;800&family=Montserrat:ital,wght@0,400;0,500;0,600;1,400&display=swap" rel="stylesheet">
<style>
:root{
  --gold:#b88a3e;
  --dark:#1d1d1d;
  --ink:#222;
  --muted:#6d6d6d;
  --band:#f2f2f2;
  --field:#ececec;
  --white:#fff;
}
*{box-sizing:border-box;margin:0;padding:0}
html,body{width:1200px;height:4566px;overflow:hidden}
body{position:relative;background:var(--white);font-family:"Montserrat",sans-serif;color:var(--ink)}
.abs{position:absolute}
.heading{font-family:"Exo 2",sans-serif;font-weight:800;text-transform:uppercase;color:var(--ink);letter-spacing:.5px}
.btn{position:absolute;display:flex;align-items:center;justify-content:center;background:var(--gold);color:#fff;font-size:11px;font-weight:600;text-transform:uppercase;letter-spacing:.5px}

/* hero */
.hero{left:0;top:0;width:1200px;height:803px;background:linear-gradient(180deg,#6f7378 0%,#8d8f86 30%,#a59d86 45%,#6a8c86 58%,#4f7a3a 72%,#3e6a2a 100%)}
.nav{left:0;top:0;width:1200px;height:71px;background:rgba(40,40,40,.55);border-bottom:1px solid rgba(255,255,255,.25)}
.logo{font-family:"Exo 2",sans-serif;font-weight:800;color:#fff;font-size:28px;letter-spacing:.5px}
.nav-links{left:430px;top:28px;display:flex;font-size:11px;color:#fff;text-transform:uppercase}
.nav-links span{padding:0 18px;border-left:1px solid rgba(255,255,255,.6);line-height:14px}
.nav-links span:first-child{border-left:0;color:var(--gold)}
.hero-frame{left:165px;top:199px;width:868px;height:242px}
.hero-title{left:0;top:218px;width:1200px;text-align:center;color:#fff;font-size:54px;line-height:58px}
.hero-sub{left:0;top:341px;width:1200px;text-align:center;color:#fff;font-size:12px}
.hero-btn{left:510px;top:376px;width:180px;height:34px;background:#fff;color:var(--ink);font-size:11px;font-weight:600;display:flex;align-items:center;justify-content:center}
.down{left:573px;top:741px;width:54px;height:80px;background:#fff;display:flex;align-items:center;justify-content:center}

/* features */
.section-title{left:0;width:1200px;text-align:center;font-size:33px}
.card{width:227px;height:321px;top:966px;background:#fff;box-shadow:0 2px 8px rgba(0,0,0,.12)}
.card .photo{width:227px;height:261px}
.card .icon{position:absolute;left:89px;top:234px;width:48px;height:48px;background:var(--gold);display:flex;align-items:center;justify-content:center}
.card p{position:absolute;top:285px;width:100%;text-align:center;font-size:11px;font-weight:600;text-transform:uppercase;line-height:15px}

/* about */
.about-photo{left:119px;top:1377px;width:516px;height:431px;background:linear-gradient(135deg,#5a3f2c,#b9a58e 45%,#7f8a6e 60%,#4a3424)}
.about-box{left:599px;top:1439px;width:482px;height:307px;background:#fff;box-shadow:0 2px 14px rgba(0,0,0,.12)}
.about-box h2{position:absolute;left:36px;top:34px;font-size:36px}
.rule{position:absolute;width:46px;height:3px;background:var(--gold)}
.about-box p{position:absolute;left:36px;top:104px;width:412px;font-size:11.5px;line-height:18.5px;color:var(--muted)}

/* amenities */
.band{left:0;top:1898px;width:1200px;height:722px;background:var(--band)}
.amenity{left:74px;width:422px;height:100px;border-bottom:1px solid #cfcfcf}
.amenity .ico{position:absolute;left:0;top:0;width:64px;height:62px;background:var(--gold);display:flex;align-items:center;justify-content:center}
.amenity h3{position:absolute;left:80px;top:16px;font-size:11.5px;font-weight:600;text-transform:uppercase}
.amenity p{position:absolute;left:80px;top:35px;font-size:10px;color:var(--muted)}
.amenity-photo{left:590px;top:2031px;width:534px;height:624px;background:linear-gradient(160deg,#3b2a20 0%,#6b5543 30%,#8e7a63 45%,#3fa0a0 65%,#2f8c92 85%,#8a7158 100%)}

/* testimonial */
.quote-text{left:250px;top:2844px;width:700px;text-align:center;font-style:italic;font-size:13px;line-height:21px;color:var(--muted)}
.arrows{display:flex;gap:2px}
.arrows span{width:46px;height:30px;display:flex;align-items:center;justify-content:center}
.arrows .prev{background:var(--dark)}
.arrows .next{background:var(--gold)}

/* gallery */
.g-photo{top:3208px;height:337px}

/* inquiry */
.footer{left:0;top:4125px;width:1200px;height:441px;background:var(--dark)}
.form{left:659px;top:3697px;width:421px;height:507px;background:#fff;box-shadow:0 2px 14px rgba(0,0,0,.12)}
.label{position:absolute;left:30px;font-size:10px;font-weight:600;text-transform:uppercase}
.field{position:absolute;left:30px;width:362px;height:41px;background:var(--field);font-size:10px;color:#8a8a8a;padding:15px 22px}
.footer-nav{left:0;top:4359px;width:1200px;display:flex;justify-content:center;font-size:11px;color:#fff;text-transform:uppercase}
.footer-nav span{padding:0 18px;border-left:1px solid rgba(255,255,255,.6);line-height:14px}
.footer-nav span:first-child{border-left:0}
.social{left:510px;top:4410px;display:flex;gap:10px}
.social span{width:36px;height:36px;background:#2e2e2e;display:block}
.social span:first-child{background:var(--gold)}
</style>
</head>
<body>

<!-- HERO -->
<section class="abs hero" role="img" aria-label="Photo of a modern two-storey villa with stone walls, glass facades and a turquoise pool on a green lawn"></section>
<header class="abs nav">
  <div class="abs logo" style="left:75px;top:19px">CASA BRISA</div>
  <nav class="abs nav-links"><span>Home</span><span>The Villa</span><span>Gallery</span><span>Experiences</span><span>Reviews</span><span>Contact</span></nav>
  <div class="btn" style="left:985px;top:18px;width:140px;height:35px">Inquire Now</div>
</header>
<svg class="abs hero-frame" viewBox="0 0 868 242" fill="none" stroke="#fff" stroke-width="2">
  <polyline points="32,1 1,1 1,241 32,241"/>
  <polyline points="836,1 867,1 867,241 836,241"/>
</svg>
<h1 class="abs heading hero-title">Luxury Living<br>In The Dominican Republic</h1>
<p class="abs hero-sub">An exclusive villa retreat offering comfort, elegance, and breathtaking views.</p>
<div class="abs hero-btn">RESERVE YOUR STAY</div>
<div class="abs down"><svg width="20" height="30" viewBox="0 0 20 30" fill="none" stroke="#222" stroke-width="1.6"><line x1="10" y1="2" x2="10" y2="27"/><polyline points="3,20 10,27 17,20"/></svg></div>

<!-- FEATURES -->
<h2 class="abs heading section-title" style="top:903px">Your Private Paradise Awaits</h2>

<div class="abs card" style="left:124px">
  <div class="photo" role="img" aria-label="Beachfront high-rise towers overlooking the ocean" style="background:linear-gradient(180deg,#9fb8d6,#c9b9a8 60%,#a88e74)"></div>
  <div class="icon"><svg width="28" height="28" viewBox="0 0 28 28" fill="none" stroke="#fff" stroke-width="1.5"><circle cx="14" cy="10" r="4"/><line x1="3" y1="20" x2="25" y2="20"/><line x1="6" y1="24" x2="22" y2="24"/></svg></div>
  <p>Spacious Suites With<br>Ocean Views</p>
</div>
<div class="abs card" style="left:367px">
  <div class="photo" role="img" aria-label="Aerial view of a pool with lounge island and tree" style="background:linear-gradient(160deg,#4fc1c9,#7fd3cc 40%,#3f8f4a 60%,#5cc4c9)"></div>
  <div class="icon"><svg width="28" height="28" viewBox="0 0 28 28" fill="none" stroke="#fff" stroke-width="1.5"><line x1="9" y1="5" x2="9" y2="19"/><line x1="17" y1="5" x2="17" y2="19"/><line x1="9" y1="10" x2="17" y2="10"/><line x1="9" y1="15" x2="17" y2="15"/><path d="M3 22q3-2 6 0t6 0 6 0 4 0"/></svg></div>
  <p>Infinity Pool &amp; Private<br>Lounge Areas</p>
</div>
<div class="abs card" style="left:608px">
  <div class="photo" role="img" aria-label="Concierge service in a wood-panelled hotel lobby" style="background:linear-gradient(160deg,#3a2a22,#7a4a36 40%,#2f5a44 75%,#d9d2c8)"></div>
  <div class="icon"><svg width="28" height="28" viewBox="0 0 28 28" fill="none" stroke="#fff" stroke-width="1.5"><path d="M5 19a9 9 0 0 1 18 0z"/><line x1="3" y1="22" x2="25" y2="22"/><line x1="14" y1="7" x2="14" y2="10"/></svg></div>
  <p>World-Class Amenities<br>&amp; Services</p>
</div>
<div class="abs card" style="left:849px">
  <div class="photo" role="img" aria-label="Green valley with lake and mountains" style="background:linear-gradient(180deg,#b7c6cf,#6e8a6a 35%,#3d6f78 55%,#3a7a2e)"></div>
  <div class="icon"><svg width="28" height="28" viewBox="0 0 28 28" fill="none" stroke="#fff" stroke-width="1.5"><rect x="4" y="6" width="20" height="16"/><path d="M14 9a3 3 0 0 1 3 3c0 2-3 5-3 5s-3-3-3-5a3 3 0 0 1 3-3z"/></svg></div>
  <p>Location Near Exclusive<br>Attractions</p>
</div>

<!-- ABOUT -->
<div class="abs about-photo" role="img" aria-label="Bedroom with wood panelling opening onto a garden terrace"></div>
<div class="abs about-box">
  <h2 class="heading">About Us</h2>
  <div class="rule" style="left:36px;top:84px"></div>
  <p>Nestled in one of the Dominican Republic’s most exclusive areas, our villa blends contemporary elegance with Caribbean warmth. Whether you’re relaxing by the pool, enjoying the stunning sunset, or exploring nearby beaches, every moment here is designed for unforgettable experiences.</p>
  <div class="btn" style="left:36px;top:211px;width:182px;height:34px">Explore The Villa</div>
</div>

<!-- AMENITIES -->
<div class="abs band"></div>
<h2 class="abs heading section-title" style="top:1954px">Designed For Comfort &amp; Style</h2>

<div class="abs amenity" style="top:2056px">
  <div class="ico"><svg width="34" height="34" viewBox="0 0 34 34" fill="none" stroke="#fff" stroke-width="1.5"><circle cx="24" cy="9" r="3"/><line x1="10" y1="8" x2="10" y2="22"/><line x1="17" y1="12" x2="17" y2="22"/><line x1="10" y1="16" x2="17" y2="16"/><path d="M4 26q4-2 8 0t8 0 8 0"/></svg></div>
  <h3>Private Infinity Pool</h3><p>Relax with stunning ocean views from your own private pool.</p>
</div>
<div class="abs amenity" style="top:2155px">
  <div class="ico"><svg width="34" height="34" viewBox="0 0 34 34" fill="none" stroke="#fff" stroke-width="1.5"><rect x="4" y="7" width="12" height="20"/><rect x="19" y="7" width="11" height="10"/><rect x="19" y="19" width="11" height="8"/><line x1="4" y1="15" x2="16" y2="15"/></svg></div>
  <h3>Fully Equipped Kitchen</h3><p>Cook like a chef or enjoy meals prepared for you.</p>
</div>
<div class="abs amenity" style="top:2256px">
  <div class="ico"><svg width="34" height="34" viewBox="0 0 34 34" fill="none" stroke="#fff" stroke-width="1.5"><rect x="8" y="12" width="12" height="16"/><line x1="14" y1="4" x2="14" y2="12"/><path d="M22 18h5v10h-5"/></svg></div>
  <h3>House Keeping Services</h3><p>Daily cleaning to keep your stay carefree.</p>
</div>
<div class="abs amenity" style="top:2354px">
  <div class="ico"><svg width="34" height="34" viewBox="0 0 34 34" fill="none" stroke="#fff" stroke-width="1.5"><rect x="4" y="14" width="26" height="9"/><rect x="7" y="9" width="8" height="5"/><rect x="19" y="9" width="8" height="5"/><line x1="5" y1="23" x2="5" y2="27"/><line x1="29" y1="23" x2="29" y2="27"/></svg></div>
  <h3>Luxury Bedrooms &amp; Bathrooms</h3><p>Elegant interiors with premium comfort and style</p>
</div>
<div class="abs amenity" style="top:2453px;border-bottom:0">
  <div class="ico"><svg width="34" height="34" viewBox="0 0 34 34" fill="none" stroke="#fff" stroke-width="1.5"><path d="M5 14l12-7 12 7"/><line x1="17" y1="7" x2="17" y2="28"/><line x1="6" y1="20" x2="28" y2="20"/><line x1="8" y1="20" x2="8" y2="28"/><line x1="26" y1="20" x2="26" y2="28"/></svg></div>
  <h3>Outdoor Dining &amp; BBQ Area</h3><p>Perfect for tropical evenings under the stars</p>
</div>
<div class="btn" style="left:74px;top:2543px;width:128px;height:34px">View More</div>
<div class="abs amenity-photo" role="img" aria-label="Covered wooden pergola beside a turquoise pool and lounge with tropical plants"></div>

<!-- TESTIMONIAL -->
<svg class="abs" style="left:563px;top:2738px" width="74" height="48" viewBox="0 0 74 48" fill="var(--gold)">
  <path d="M2 30a16 16 0 0 1 16-16c-4-6-10-9-10-9 12 0 24 10 26 24a16 16 0 1 1-32 1z"/>
  <path d="M40 30a16 16 0 0 1 16-16c-4-6-10-9-10-9 12 0 24 10 26 24a16 16 0 1 1-32 1z"/>
</svg>
<h2 class="abs heading section-title" style="top:2793px">What Our Client Says</h2>
<p class="abs quote-text">Our guests come for the luxury, but stay for the unforgettable memories. From breathtaking views to personalized service, every experience at our villa is designed to exceed expectations. See what past visitors have to say about their stay in paradise.</p>
<p class="abs" style="left:0;top:2918px;width:1200px;text-align:center;font-size:12px;font-weight:500">ELENA &amp; MARCO</p>
<div class="abs" style="left:0;top:2944px;width:1200px;text-align:center;color:var(--gold);font-size:17px;letter-spacing:3px">★★★★★</div>
<div class="abs arrows" style="left:553px;top:2994px">
  <span class="prev"><svg width="20" height="10" viewBox="0 0 20 10" fill="none" stroke="#fff" stroke-width="1.4"><line x1="1" y1="5" x2="19" y2="5"/><polyline points="6,1 1,5 6,9"/></svg></span>
  <span class="next"><svg width="20" height="10" viewBox="0 0 20 10" fill="none" stroke="#fff" stroke-width="1.4"><line x1="1" y1="5" x2="19" y2="5"/><polyline points="14,1 19,5 14,9"/></svg></span>
</div>

<!-- GALLERY -->
<h2 class="abs heading section-title" style="top:3106px;line-height:41px">Discover The Beauty Of Every<br>Corner</h2>
<div class="abs g-photo" style="left:76px;width:245px;background:linear-gradient(180deg,#2f7fc4,#5b99c9 45%,#3f5a3a 75%,#6f7a6a)" role="img" aria-label="Villa entrance with palm trees and a parked car"></div>
<div class="abs g-photo" style="left:333px;width:534px;background:linear-gradient(180deg,#1f6db5,#4c8fc7 40%,#7a6752 62%,#2d5f77 85%,#243440)" role="img" aria-label="Villa facade lit at dusk behind a long pool and palm trees"></div>
<div class="abs g-photo" style="left:881px;width:243px;background:linear-gradient(180deg,#3c85c6,#7aaad0 45%,#4d7a3c 72%,#8fa37c)" role="img" aria-label="Garden courtyard with palm trees and a paved path"></div>
<div class="abs arrows" style="left:553px;top:3577px">
  <span class="prev"><svg width="20" height="10" viewBox="0 0 20 10" fill="none" stroke="#fff" stroke-width="1.4"><line x1="1" y1="5" x2="19" y2="5"/><polyline points="6,1 1,5 6,9"/></svg></span>
  <span class="next"><svg width="20" height="10" viewBox="0 0 20 10" fill="none" stroke="#fff" stroke-width="1.4"><line x1="1" y1="5" x2="19" y2="5"/><polyline points="14,1 19,5 14,9"/></svg></span>
</div>

<!-- INQUIRY -->
<p class="abs" style="left:119px;top:3817px;font-size:10.5px;font-weight:600">RESERVATION INQUIRY</p>
<h2 class="abs heading" style="left:118px;top:3836px;font-size:34px">Plan Your Stay With Us</h2>
<p class="abs" style="left:119px;top:3890px;width:440px;font-size:11.5px;line-height:19px;color:var(--muted)">Ready to experience tropical luxury? Send us your preferred dates and we’ll help arrange every detail of your stay.</p>

<footer class="abs footer">
  <div class="abs logo" style="left:0;top:163px;width:1200px;text-align:center;font-size:38px">CASA BRISA</div>
  <nav class="abs footer-nav" style="top:234px"><span>Home</span><span>The Villa</span><span>Gallery</span><span>Experiences</span><span>Reviews</span><span>Contact</span></nav>
  <div class="abs social" style="top:285px"><span></span><span></span><span></span><span></span></div>
  <div class="abs" style="left:75px;top:372px;width:1050px;height:1px;background:rgba(255,255,255,.35)"></div>
  <div class="abs" style="left:1143px;top:354px;width:37px;height:37px;background:var(--gold);display:flex;align-items:center;justify-content:center"><svg width="12" height="8" viewBox="0 0 12 8" fill="none" stroke="#fff" stroke-width="1.6"><polyline points="1,7 6,2 11,7"/></svg></div>
  <p class="abs" style="left:0;top:401px;width:1200px;text-align:center;font-size:10.5px;color:#fff">2025 COPYRIGHT LUXURY PROPERTY. ALL RIGHTS RESERVED.</p>
</footer>

<form class="abs form">
  <span class="label" style="top:34px">Name*</span><div class="field" style="top:51px">Enter Your Name</div>
  <span class="label" style="top:107px">Email*</span><div class="field" style="top:124px">Enter Your Email</div>
  <span class="label" style="top:180px">Phone*</span><div class="field" style="top:197px">Enter Your Phone</div>
  <span class="label" style="top:253px">Address*</span><div class="field" style="top:270px">Enter Your Address</div>
  <span class="label" style="top:328px">Message*</span><div class="field" style="top:343px;height:86px;padding-top:12px">Please Send Your Message</div>
  <div class="btn" style="left:140px;top:444px;width:140px;height:32px">Submit Now</div>
</form>

</body>
</html>
```